Online Sports Booking Business

We need a flyer design for a new company based in Bahrain called "GoalDash.net".

GoalDash is an online booking service for the sport field in Bahrain. We would like to design a flyer in away that reflects our idea and the type of customers who will benefit from the service. You can visit the website in order to get an idea about the service provided.

Service Description:
Simply sign up, search and choose, book and pay for any sports venue or activity using your own computer or smartphone.

- Choose from different sport centers and activities in Bahrain
- Compare based on unbiased reviews by real people
- Check for availability
- Book and pay online in less than a minute
- Track, manage, modify and cancel your bookings online
- Receive automatic notifications (upon request) whenever your favorite venue/activity is available
- Rate and post reviews about your experience

We would like the design to use the color green as a background, nice and casual visual icons and images to show the above steps. The final design should communicate the value and benefits in a joyful and casual way that is attractive to the sport lovers.
Updates

Target Market(s)

english speakers aged 18-45 who are into sports.

Industry/Entity Type

Computer

Font styles to use
Sans Serif
Other font styles liked:
• something similar to the logo

Colors
add136
9bcb3c
ffffff

Requirements
Must have
• Please use the content in the attachment. Logo can be taken from goaldash.net
Nice to have
• steps and benefits to use icons and visual presentations rather than dull text only.

```html
<!DOCTYPE html>
<html lang="en">
<head>
<meta charset="utf-8">
<title>GoalDash.net Flyer</title>
<link rel="stylesheet" href="https://fonts.googleapis.com/css2?family=Roboto:wght@700;900&family=Nunito:wght@800&family=Open+Sans:wght@400&display=swap">
<style>
  :root {
    --lime: #add136;
    --lime-deep: #9bcb3c;
    --white: #ffffff;
    --green-light: #6d9a35;
    --green-mid: #527f27;
    --green-dark: #3a6219;
    --text-green: #4d7a22;
    --text-grey: #555b52;
    --panel: #eeefee;
    --rule: #c4c8c2;
  }
  * { box-sizing: border-box; margin: 0; padding: 0; }
  html, body { width: 932px; height: 1200px; overflow: hidden; }
  body { background: var(--green-dark); }

  .flyer {
    position: relative;
    width: 932px;
    height: 1200px;
    overflow: hidden;
    background: radial-gradient(ellipse at 45% 50%, var(--green-light) 0%, var(--green-mid) 55%, var(--green-dark) 100%);
    font-family: "Roboto", Arial, sans-serif;
  }

  .hero { position: absolute; left: 0; top: 0; width: 932px; height: 340px; }

  .headline {
    position: absolute; left: 62px; top: 44px; width: 860px;
    color: var(--white); font-weight: 700; font-size: 62px; line-height: 76px;
    letter-spacing: 1.5px;
    text-shadow: 0 2px 6px rgba(0,0,0,0.35);
  }

  .tag {
    position: absolute; left: 468px; top: 226px;
    padding: 14px 30px 12px;
    background: var(--lime);
    color: var(--white);
    border-radius: 14px;
    font-weight: 700; font-size: 46px; line-height: 1; letter-spacing: 1px;
    transform: rotate(-10deg);
    box-shadow: 0 6px 10px rgba(0,0,0,0.35);
  }

  .brand {
    position: absolute; left: 62px; top: 358px; width: 452px; height: 100px;
    display: flex; align-items: center; gap: 16px;
    padding-left: 12px;
    background: linear-gradient(90deg, rgba(40,70,20,0.35), rgba(40,70,20,0));
  }
  .brand-dot { width: 36px; height: 36px; border-radius: 50%; background: var(--white); flex: none; }
  .brand-name { color: var(--white); font-family: "Nunito", sans-serif; font-weight: 800; font-size: 50px; }

  .ball { position: absolute; left: 648px; top: 400px; width: 224px; height: 220px; }

  .intro {
    position: absolute; left: 64px; top: 490px; width: 600px;
    color: var(--white); font-weight: 700; font-size: 31px; line-height: 42px;
    letter-spacing: 0.5px;
    text-shadow: 0 2px 4px rgba(0,0,0,0.3);
  }
  .intro .domain { color: var(--lime); }

  .promise {
    position: absolute; left: 64px; top: 628px; width: 860px;
    color: var(--lime); font-weight: 700; font-size: 35px; line-height: 62px;
    letter-spacing: 0.5px;
    text-shadow: 0 2px 4px rgba(0,0,0,0.3);
  }
  .promise .free { color: var(--white); font-size: 50px; margin-left: 8px; }

  .panel {
    position: absolute; left: 62px; top: 758px; width: 798px; height: 358px;
    background: linear-gradient(180deg, #ffffff 0%, var(--panel) 100%);
    border-radius: 14px;
    box-shadow: 0 8px 14px rgba(0,0,0,0.35);
    display: flex;
  }
  .panel-lead {
    width: 276px; padding: 16px 10px 0 22px;
    color: var(--text-green); font-family: "Nunito", sans-serif; font-weight: 800;
    font-size: 26px; line-height: 36.5px;
    white-space: nowrap;
  }
  .panel-rule { width: 2px; margin: 18px 0; background: var(--rule); }
  .benefits {
    list-style: none; padding: 24px 20px 0 28px; flex: 1;
    font-family: "Open Sans", sans-serif; font-size: 16.5px; line-height: 23px; color: var(--text-grey);
    white-space: nowrap;
  }
  .benefits li { display: flex; gap: 10px; margin-bottom: 9px; }
  .benefits svg { flex: none; margin-top: 4px; }

  .signoff {
    position: absolute; left: 0; top: 1124px; width: 932px; text-align: center;
    color: var(--lime); font-weight: 700; font-size: 52px; letter-spacing: 1px;
    text-shadow: 0 2px 4px rgba(0,0,0,0.3);
  }
</style>
</head>
<body>
<main class="flyer">
  <svg class="hero" viewBox="0 0 932 340">
    <defs>
      <linearGradient id="grass" x1="0" y1="0" x2="0" y2="1">
        <stop offset="0" stop-color="#9fd04a"/>
        <stop offset="0.55" stop-color="#6fae2c"/>
        <stop offset="1" stop-color="#4f8a1c"/>
      </linearGradient>
    </defs>
    <path d="M0 250 Q300 320 560 288 Q760 262 932 222 V246 Q760 290 560 312 Q300 340 0 278 Z" fill="var(--lime)"/>
    <path d="M0 0 H932 V222 Q760 262 560 288 Q300 320 0 250 Z" fill="url(#grass)" role="img" aria-label="Photograph of a close-up green grass field"/>
  </svg>

  <h1 class="headline">Pick your Pitch NOW at<br>goaldash.net</h1>
  <div class="tag">Game on!</div>

  <div class="brand">
    <span class="brand-dot"></span>
    <span class="brand-name">GoalDash.net</span>
  </div>

  <svg class="ball" viewBox="0 0 224 220" role="img" aria-label="Illustration of a black and white football">
    <defs>
      <radialGradient id="ballShade" cx="0.4" cy="0.35" r="0.7">
        <stop offset="0" stop-color="#ffffff"/>
        <stop offset="0.7" stop-color="#d9dad8"/>
        <stop offset="1" stop-color="#8c8e8a"/>
      </radialGradient>
    </defs>
    <ellipse cx="115" cy="204" rx="100" ry="10" fill="rgba(0,0,0,0.35)"/>
    <circle cx="112" cy="100" r="98" fill="url(#ballShade)"/>
  </svg>

  <p class="intro">A click away from your favorite<br>sports venue <span class="domain">goaldash.net</span></p>

  <p class="promise">The place where you can instantly<br>reserve your sport activity <span class="free">It’s FREE!</span></p>

  <section class="panel">
    <p class="panel-lead">Simply sign up,<br>search and<br>choose, book<br>and pay for any<br>sports venue or<br>activity using<br>your own<br>computer or<br>smartphone.</p>
    <div class="panel-rule"></div>
    <ul class="benefits">
      <li><svg width="16" height="16" viewBox="0 0 16 16"><circle cx="8" cy="8" r="8" fill="var(--lime-deep)"/><path d="M4 8.5 L7 11 L12 5" stroke="#fff" stroke-width="2" fill="none"/></svg><span>Choose from different sport centers and<br>activities in Bahrain</span></li>
      <li><svg width="16" height="16" viewBox="0 0 16 16"><circle cx="8" cy="8" r="8" fill="var(--lime-deep)"/><path d="M4 8.5 L7 11 L12 5" stroke="#fff" stroke-width="2" fill="none"/></svg><span>Compare based on unbiased reviews by real<br>people</span></li>
      <li><svg width="16" height="16" viewBox="0 0 16 16"><circle cx="8" cy="8" r="8" fill="var(--lime-deep)"/><path d="M4 8.5 L7 11 L12 5" stroke="#fff" stroke-width="2" fill="none"/></svg><span>Check for availability</span></li>
      <li><svg width="16" height="16" viewBox="0 0 16 16"><circle cx="8" cy="8" r="8" fill="var(--lime-deep)"/><path d="M4 8.5 L7 11 L12 5" stroke="#fff" stroke-width="2" fill="none"/></svg><span>Book and pay online in less than a minute</span></li>
      <li><svg width="16" height="16" viewBox="0 0 16 16"><circle cx="8" cy="8" r="8" fill="var(--lime-deep)"/><path d="M4 8.5 L7 11 L12 5" stroke="#fff" stroke-width="2" fill="none"/></svg><span>Track, manage, modify and cancel your<br>bookings online</span></li>
      <li><svg width="16" height="16" viewBox="0 0 16 16"><circle cx="8" cy="8" r="8" fill="var(--lime-deep)"/><path d="M4 8.5 L7 11 L12 5" stroke="#fff" stroke-width="2" fill="none"/></svg><span>Receive automatic notifications (upon request)<br>whenever your favorite venue/activity is<br>available</span></li>
      <li><svg width="16" height="16" viewBox="0 0 16 16"><circle cx="8" cy="8" r="8" fill="var(--lime-deep)"/><path d="M4 8.5 L7 11 L12 5" stroke="#fff" stroke-width="2" fill="none"/></svg><span>Rate and post reviews about your experience</span></li>
    </ul>
  </section>

  <p class="signoff">Have Fun!!</p>
</main>
</body>
</html>
```